Tallow Crest Business Card

We need a business card designed for a a company called "Tallow Crest". We offer consulting, coaching and training to business leaders and coaches (across the world) using the latest findings in neuroscience, social and emotional intelligence and positive psychology. The final design should communicate the use of brain science to create sustainable relationships.

The card should be doublesided. The logo is attached and names and titles will be provided to the successful designer. Thank you.

Industry/Entity Type

Training

```html
<!DOCTYPE html>
<html lang="en">
<head>
<meta charset="utf-8">
<title>Tallow Crest Business Card</title>
<link rel="stylesheet" href="https://fonts.googleapis.com/css2?family=Open+Sans:wght@400;600;700&display=swap">
<style>
  :root {
    --backdrop: #e9e9e9;
    --paper: #f5f5f5;
    --ink: #231f20;
    --brand-blue: #1b80b8;
    --brand-green: #9cc43a;
    --rule-grey: #a9a9a9;
    --text-dark: #2a2a2a;
  }
  * { box-sizing: border-box; margin: 0; padding: 0; }
  html, body {
    width: 1200px; height: 960px; overflow: hidden;
    background: var(--backdrop);
    font-family: "Open Sans", Arial, sans-serif;
  }
  .canvas {
    position: relative; width: 1200px; height: 960px;
    display: flex; align-items: center; justify-content: center; gap: 40px;
  }
  .card {
    position: relative; width: 540px; height: 309px; overflow: hidden;
    box-shadow: 0 2px 10px rgba(0,0,0,0.12);
  }
  /* Front */
  .card-front { background: var(--paper); color: var(--text-dark); }
  .brand {
    position: absolute; display: flex; align-items: center; gap: 8px;
    font-weight: 700; color: var(--brand-blue); white-space: nowrap;
  }
  .brand-dot { border-radius: 50%; background: var(--brand-green); flex: none; }
  .card-front .brand { left: 30px; top: 42px; font-size: 24px; }
  .card-front .brand-dot { width: 14px; height: 14px; }
  .divider {
    position: absolute; left: 30px; right: 40px; top: 96px;
    height: 1px; background: var(--rule-grey);
  }
  .address {
    position: absolute; left: 30px; top: 106px;
    font-size: 12.5px; line-height: 17px;
  }
  .contacts {
    position: absolute; left: 30px; top: 150px;
    display: grid; grid-template-columns: 170px auto; row-gap: 2px;
    font-size: 12.5px; line-height: 17px;
  }
  .contact-item { display: flex; align-items: center; gap: 6px; }
  .contact-item svg { width: 12px; height: 12px; flex: none; }
  .at-icon { color: var(--brand-blue); font-weight: 700; width: 12px; font-size: 12px; }
  .person {
    position: absolute; right: 40px; top: 158px; text-align: right;
  }
  .person-name { color: var(--brand-blue); font-weight: 700; font-size: 13.5px; line-height: 18px; }
  .person-title { font-size: 12.5px; line-height: 17px; }
  .edge-bands { position: absolute; left: 0; right: 0; bottom: 0; height: 40px; }
  .band-line { position: absolute; left: 0; right: 0; height: 2px; background: var(--brand-blue); }
  .band-line.upper { top: 6px; }
  .band-line.lower { bottom: 4px; }
  .band-ink { position: absolute; left: 0; right: 0; top: 12px; height: 16px; background: var(--ink); }
  /* Back */
  .card-back { background: var(--ink); display: flex; align-items: center; justify-content: center; }
  .card-back .brand { position: static; font-size: 30px; }
  .card-back .brand-dot { width: 18px; height: 18px; }
</style>
</head>
<body>
<main class="canvas">
  <section class="card card-front" aria-label="Card front">
    <div class="brand"><span class="brand-dot"></span>Tallow Crest</div>
    <div class="divider"></div>
    <p class="address">48 Lantern Row, Suite 310, P.O. Box 2219<br>Fernbrook, Ohio 43021-2219</p>
    <div class="contacts">
      <span class="contact-item">
        <svg viewBox="0 0 12 12" aria-label="Phone"><path fill="#1b80b8" d="M1 3.5C1 2 2.5 1.5 6 1.5s5 .5 5 2v1H8.5V3.3h-5V4.5H1zM2.5 5.5h7L11 10.5H1z"/><circle cx="6" cy="8" r="1.3" fill="#f5f5f5"/></svg>
        555.018.2741
      </span>
      <span class="contact-item"><span class="at-icon">@</span>rudd@tallowcrest.com</span>
      <span class="contact-item">
        <svg viewBox="0 0 12 12" aria-label="Mobile"><rect x="3" y="0.5" width="6" height="11" rx="1" fill="#1b80b8"/><rect x="4" y="2" width="4" height="6" fill="#f5f5f5"/></svg>
        555.018.2741
      </span>
      <span class="contact-item">
        <svg viewBox="0 0 12 12" aria-label="Website"><circle cx="6" cy="6" r="5" fill="none" stroke="#1b80b8" stroke-width="1.4"/><path d="M1 6h10M6 1v10" stroke="#1b80b8" stroke-width="1.1"/></svg>
        www.tallowcrest.com
      </span>
    </div>
    <div class="person">
      <p class="person-name">Marion J. Rudd</p>
      <p class="person-title">Director</p>
    </div>
    <div class="edge-bands">
      <div class="band-line upper"></div>
      <div class="band-ink"></div>
      <div class="band-line lower"></div>
    </div>
  </section>
  <section class="card card-back" aria-label="Card back">
    <div class="brand"><span class="brand-dot"></span>Tallow Crest</div>
  </section>
</main>
</body>
</html>
```